Poster Design Project

Need a design for a music festival called Counter-Lanternweek

The design needs to have areas for the following:
- Band Names
- DJ Names
- Sponsor Names and Logos
- Event location, Date & Time

Industry/Entity Type

Festival

```html
<!DOCTYPE html>
<html lang="en">
<head>
<meta charset="utf-8">
<title>Counter-Lanternweek — Festival Poster</title>
<link rel="stylesheet" href="https://fonts.googleapis.com/css2?family=Nunito:wght@800;900&display=swap">
<style>
  :root {
    --bg-deep: #07040b;
    --bg-glow: #2b0f3d;
    --ink-white: #ffffff;
    --ink-silver: #cfcfd6;
    --tag-orange: #f29a16;
    --tag-yellow: #f8d21c;
    --tag-ink: #1d1208;
    --title-yellow: #f6e51c;
    --title-orange: #f7a21a;
    --title-pink: #ef3db4;
    --title-violet: #b247e6;
    --date-gold: #f2a814;
    --address-magenta: #d624e6;
  }
  * { box-sizing: border-box; margin: 0; padding: 0; }
  html, body { width: 800px; height: 1200px; overflow: hidden; background: var(--bg-deep); }
  .poster {
    position: relative;
    width: 800px;
    height: 1200px;
    overflow: hidden;
    font-family: "Nunito", "Arial Rounded MT Bold", sans-serif;
    font-weight: 900;
    background:
      radial-gradient(ellipse 90% 60% at 50% 78%, var(--bg-glow) 0%, rgba(43,15,61,0.55) 45%, rgba(7,4,11,0) 80%),
      var(--bg-deep);
  }

  /* ---------- Masthead ---------- */
  .masthead {
    position: absolute;
    left: 70px;
    top: 250px;
    transform-origin: 0 0;
    transform: rotate(-13deg);
  }
  .title-tag {
    position: absolute;
    left: 95px;
    top: -150px;
    padding: 2px 14px 6px;
    font-size: 58px;
    letter-spacing: -1px;
    color: var(--tag-ink);
    background: linear-gradient(100deg, var(--tag-orange), var(--tag-yellow) 60%, var(--tag-orange));
    white-space: nowrap;
    line-height: 1.05;
  }
  .title-main {
    position: absolute;
    left: 0;
    top: -92px;
    font-size: 108px;
    letter-spacing: -3px;
    line-height: 1;
    white-space: nowrap;
    background: linear-gradient(90deg, var(--title-yellow) 0%, var(--title-orange) 30%, var(--title-pink) 52%, var(--title-violet) 72%, var(--ink-white) 92%);
    -webkit-background-clip: text;
    background-clip: text;
    color: transparent;
    filter: drop-shadow(0 4px 6px rgba(0,0,0,0.6));
  }
  .event-date {
    position: absolute;
    left: 75px;
    top: 40px;
    font-size: 27px;
    line-height: 1.15;
    color: var(--date-gold);
    text-align: right;
    white-space: nowrap;
    text-shadow: 0 2px 4px rgba(0,0,0,0.7);
  }
  .event-address {
    position: absolute;
    left: 330px;
    top: 24px;
    font-size: 29px;
    line-height: 1.15;
    color: var(--address-magenta);
    white-space: nowrap;
    text-shadow: 0 2px 4px rgba(0,0,0,0.7);
  }

  /* ---------- Lineup ---------- */
  .lineup {
    position: absolute;
    left: 28px;
    top: 535px;
    transform-origin: 0 0;
    transform: rotate(-13deg);
    white-space: nowrap;
  }
  .lineup-row {
    display: flex;
    align-items: baseline;
    gap: 22px;
    height: 78px;
  }
  .act {
    line-height: 1;
    letter-spacing: -1px;
    background: linear-gradient(180deg, var(--ink-white) 45%, var(--ink-silver));
    -webkit-background-clip: text;
    background-clip: text;
    color: transparent;
    filter: drop-shadow(0 4px 4px rgba(0,0,0,0.75));
  }
  .act--headliner { font-size: 68px; }
  .act--large { font-size: 58px; }
  .act--medium { font-size: 40px; }
  .act--small { font-size: 34px; }

  /* ---------- Sponsors ---------- */
  .sponsors {
    position: absolute;
    left: 262px;
    top: 1016px;
    transform-origin: 0 0;
    transform: rotate(-11deg);
    white-space: nowrap;
  }
  .sponsor-row {
    display: flex;
    align-items: baseline;
    height: 30px;
  }
  .sponsor {
    line-height: 1;
    letter-spacing: -0.3px;
    color: var(--ink-white);
    text-shadow: 0 2px 3px rgba(0,0,0,0.8);
  }
  .sponsor--xl { font-size: 26px; }
  .sponsor--l { font-size: 22px; }
  .sponsor--s { font-size: 17px; }
</style>
</head>
<body>
<main class="poster">

  <header class="masthead">
    <span class="title-tag">Counter-</span>
    <h1 class="title-main">Lanternweek</h1>
    <p class="event-date">22 July 2012<br>11 AM- Midnight</p>
    <p class="event-address">412 W. 52nd St<br>Riverton, NC 28999</p>
  </header>

  <section class="lineup" aria-label="Lineup">
    <div class="lineup-row">
      <span class="act act--large" style="font-size:52px">Quiet Harbor</span>
      <span class="act act--small">Odd Theory</span>
    </div>
    <div class="lineup-row" style="padding-left:80px">
      <span class="act act--large">Band Names</span>
      <span class="act act--large">Band Names</span>
    </div>
    <div class="lineup-row" style="margin-left:-90px">
      <span class="act act--large">Band Names</span>
      <span class="act act--medium">Band Names</span>
      <span class="act act--medium">Band Names</span>
    </div>
    <div class="lineup-row" style="margin-left:-130px">
      <span class="act act--medium">Band Names</span>
      <span class="act act--headliner">The Measured</span>
      <span class="act act--large">Band Names</span>
    </div>
    <div class="lineup-row" style="margin-left:-110px">
      <span class="act act--large">Band Names</span>
      <span class="act act--medium">Band Names</span>
    </div>
    <div class="lineup-row" style="padding-left:10px">
      <span class="act act--large">Band Names</span>
      <span class="act act--medium">Band Names</span>
    </div>
  </section>

  <section class="sponsors" aria-label="Sponsors">
    <div class="sponsor-row" style="padding-left:200px;gap:40px">
      <span class="sponsor sponsor--l">SPONSORS</span>
      <span class="sponsor sponsor--s">Odd Theory</span>
    </div>
    <div class="sponsor-row" style="padding-left:110px;gap:50px">
      <span class="sponsor sponsor--xl">Band Names</span>
      <span class="sponsor sponsor--s">Band Names</span>
    </div>
    <div class="sponsor-row" style="gap:16px">
      <span class="sponsor sponsor--xl">Band Names</span>
      <span class="sponsor sponsor--l">Band Names</span>
      <span class="sponsor sponsor--xl">SPONSORS</span>
    </div>
    <div class="sponsor-row" style="gap:56px">
      <span class="sponsor sponsor--s">Band Names</span>
      <span class="sponsor sponsor--s">Band Names</span>
      <span class="sponsor sponsor--s">Band Names</span>
    </div>
    <div class="sponsor-row" style="padding-left:10px;gap:18px">
      <span class="sponsor sponsor--l">Band Names</span>
      <span class="sponsor sponsor--xl">Band Names</span>
      <span class="sponsor sponsor--xl">Band Names</span>
    </div>
    <div class="sponsor-row" style="padding-left:370px">
      <span class="sponsor sponsor--s">Band Names</span>
    </div>
  </section>

</main>
</body>
</html>
```